App Design for FlavorTrek

We need an app design for a new app called FlavorTrek, which is an app designed to inspire exploration through personalized recipe generation, local restaurant discoveries, and a vibrant community platform. It caters to food enthusiasts looking to explore global cuisines or find the best local dining spots, offering a premium experience with selected features available for free.

-------UPDATED-----
This app will be AI Driven and may not be heavily dependent on media (images,videos) at first, especially for the Recipe generator feature. Our goal is to still have attractive UI. The core functionalities we are looking are the following
1. Recipe Generator: Either user choose a specific cuisine(italian,spanish), or user inputs ingredients and get recipe, or get recipe for different occasions (xmas, thanksgiving ) and get a randomly get recipe to cook, plain simple. We expect the recipes to be displayed in clear and not too generic manner starting with ingredients and expected duration at top and then step by step guide. We also intend to enable premium users to have playful action button or icon to get unlimited recipes generated until they find what they like and also have save for later feature. These premium features should be disabled for free users and prompted to subscribe if they click them with nice popup
2. Restaurant Recommendation - will have selected pictures and will be based on inputs such as zip code and other filters such as cousine types. Premium users can filter by price range, get unlimited recommendation, see actual price range in the recommendation and can save for later where they can find it later. Free users cannot filter by price (disabled) and should see it hidden in the recommendation
3. Meal Planning - will include just simple and random meal plan with just one button or limited interaction for free, users need to subscribe to get features such as customized plan such as considering allergies or diet preferences. Premium users can also get a shopping checklist of ingredients for weekly meal preps and their step by step guide for each meal recipe.
2. Community Sharing: users can view posts and engage with community content
Updates

Hello Designers,

The initial price was not fair for the work. So I have increased it. There will also be $50-100 bonus for those who come up with great designs or for those who incorporate interesting stuff. Thank you! Much appreciated 🙏

Colors
0054AA
0677BA
7BADD7
CADEEF
E8F1F8
0094D4
00A9DD
6FCCEA
C7EBF8
E9F6FB
00AB8E
00BBA5
67D7C9
C6EFE9
E9F9F6
FFC000
F8CF3A
FAE287
FDF2CF
FEFAEE
F0912C
F2A743
F7CA91
FBE8D2
FDF5EE
EE7325
F08F49
F5BC92
FAE3D3
FDF4ED
A7469A
B969AE
D3A5CF
EDDBEB
F8F0F9
6B429C
8869AF
B7A5CE
E3DAEB
F3F0F8

```html
<!DOCTYPE html>
<html lang="en">
<head>
<meta charset="utf-8">
<title>FlavorTrek App Screens</title>
<link rel="stylesheet" href="https://fonts.googleapis.com/css2?family=Jost:wght@600&family=Poppins:wght@400;500;600&display=swap">
<style>
  :root {
    --brand: #1f5aa6;
    --band: #0a82f2;
    --ink: #1b1b1b;
    --muted: #8a8a8a;
    --line: #c9c9c9;
    --link: #1f6fd1;
    --dark: #3a3a3a;
    --white: #ffffff;
  }
  * { box-sizing: border-box; margin: 0; padding: 0; }
  html, body { width: 1200px; height: 697px; overflow: hidden; background: var(--white); }
  body { font-family: "Poppins", sans-serif; color: var(--ink); position: relative; }
  .backdrop { position: absolute; inset: 0; }
  .screen {
    position: absolute; top: 83px; width: 254px; height: 531px;
    background: var(--white); box-shadow: 0 8px 22px rgba(0,0,0,.18); overflow: hidden;
  }
  .screen--signup { left: 128px; }
  .screen--login { left: 473px; }
  .screen--home { left: 818px; }
  .abs { position: absolute; }
  .logo { font-family: "Jost", sans-serif; font-weight: 600; color: var(--brand); letter-spacing: 1px; }
  .logo--large { left: 0; width: 100%; text-align: center; top: 28px; font-size: 37px; line-height: 44px; }
  .label { left: 13px; font-size: 10.5px; line-height: 12px; }
  .field {
    left: 12px; width: 230px; height: 35px; border: 1px solid var(--line); border-radius: 3px;
    padding-left: 11px; display: flex; align-items: center; font-size: 10.5px; color: var(--muted);
  }
  .field--active { border: 1.5px solid var(--brand); }
  .field--filled { color: var(--ink); font-weight: 600; }
  .field .eye { position: absolute; right: 8px; top: 11px; }
  .btn {
    left: 12px; width: 230px; height: 35px; background: var(--brand); border-radius: 3px;
    color: var(--white); font-size: 11px; font-weight: 600; display: flex; align-items: center; justify-content: center;
  }
  .divider { left: 23px; width: 208px; display: flex; align-items: center; gap: 8px; font-size: 9.5px; line-height: 12px; color: var(--muted); }
  .divider::before, .divider::after { content: ""; flex: 1; height: 1px; background: #8a8a8a; }
  .social {
    width: 40px; height: 40px; border-radius: 50%; background: var(--white);
    box-shadow: 0 1px 4px rgba(0,0,0,.14); display: flex; align-items: center; justify-content: center;
    font-size: 8.5px; font-weight: 500; color: var(--ink); margin-left: -20px; margin-top: -20px;
  }
  .footnote { left: 0; width: 100%; text-align: center; font-size: 10px; line-height: 13px; }
  .footnote a { color: var(--link); text-decoration: underline; }
  .forgot { right: 12px; font-size: 9.5px; line-height: 12px; }
  /* home */
  .logo--small { left: 7px; top: 8px; font-size: 27px; line-height: 32px; }
  .icon-btn {
    width: 26px; height: 26px; border-radius: 50%; margin-left: -13px; margin-top: -13px;
    display: flex; align-items: center; justify-content: center;
  }
  .icon-btn--bell { background: var(--brand); border: 1px solid #16457f; }
  .avatar { background: linear-gradient(160deg, #d8d8d8, #8d7a6b); border: 1px solid #999; }
  .search-label { left: 12px; top: 47px; font-size: 10.5px; }
  .search-box {
    left: 12px; top: 62px; width: 230px; height: 30px; border: 1.5px solid var(--brand); border-radius: 3px;
    font-size: 9px; color: var(--muted); padding-left: 10px; display: flex; align-items: center;
  }
  .search-go {
    position: absolute; right: 4px; top: 3px; width: 21px; height: 21px; border-radius: 50%;
    background: var(--brand); display: flex; align-items: center; justify-content: center;
  }
  .section-title { left: 12px; font-size: 13px; font-weight: 500; }
  .recipe-photo { width: 63px; height: 55px; border: 1px solid var(--brand); border-radius: 2px; }
  .recipe-name { font-size: 9px; line-height: 10px; }
  .recipe-price { font-size: 7.5px; line-height: 9px; }
  .add { width: 12px; height: 12px; margin-left: -6px; margin-top: -6px; }
  .venue-photo { width: 96px; height: 85px; border: 1px solid var(--brand); border-radius: 2px; }
  .venue-name { font-size: 12px; }
  .promo {
    left: 0; top: 450px; width: 100%; height: 52px; background: var(--dark); color: var(--white);
    font-size: 11px; font-weight: 500; line-height: 14.5px; text-align: center; padding-top: 6px;
  }
  .btn--promo { top: 490px; }
  .tone-taco { background: linear-gradient(135deg, #6a4a2a, #b58a4a 50%, #4f6b2a); }
  .tone-potato { background: linear-gradient(135deg, #2a2418, #8a7a52 55%, #3a3a2a); }
  .tone-stew { background: linear-gradient(135deg, #b07a4a, #9a3a1e 55%, #3a2a22); }
  .tone-pasta { background: linear-gradient(135deg, #2a2a2a, #c06a2a 55%, #3a3028); }
  .tone-chicken { background: linear-gradient(135deg, #3a3a3a, #b07a42 55%, #a82a1e); }
  .tone-stirfry { background: linear-gradient(135deg, #3a3f48, #b8402a 55%, #2a2a2a); }
  .tone-hall { background: linear-gradient(160deg, #8a8f88, #a0683a 60%, #5a3a22); }
  .tone-dining { background: linear-gradient(160deg, #4a3a2e, #b0582a 55%, #6a3a22); }
</style>
</head>
<body>
  <svg class="backdrop" width="1200" height="697" aria-hidden="true">
    <polygon points="0,593 971,0 1200,0 1200,100 214,697 0,697" fill="var(--band)"/>
  </svg>

  <!-- Sign up -->
  <section class="screen screen--signup">
    <div class="abs logo logo--large">FlavorTrek</div>
    <div class="abs label" style="top:96px">Email</div>
    <div class="abs field field--active" style="top:112px">Enter your Email</div>
    <div class="abs label" style="top:158px">Username</div>
    <div class="abs field field--active field--filled" style="top:174px">Marcus Lenn</div>
    <div class="abs label" style="top:222px">Password</div>
    <div class="abs field" style="top:238px">Enter your password
      <svg class="eye" width="14" height="12" viewBox="0 0 14 12"><path d="M1 6c2-3.5 10-3.5 12 0-2 3.5-10 3.5-12 0z" fill="none" stroke="#999" stroke-width="1"/><circle cx="7" cy="6" r="1.8" fill="none" stroke="#999"/><line x1="2" y1="11" x2="12" y2="1" stroke="#999"/></svg>
    </div>
    <div class="abs label" style="top:282px">Zipcode</div>
    <div class="abs field" style="top:298px">Enter your Zipcode</div>
    <div class="abs btn" style="top:349px">Create Account</div>
    <div class="abs divider" style="top:400px">Or Continue With</div>
    <div class="abs social" style="left:78px;top:451px">Orbly</div>
    <div class="abs social" style="left:129px;top:451px">Chatter</div>
    <div class="abs social" style="left:180px;top:451px">Pomme</div>
    <p class="abs footnote" style="top:505px">Already have an account? <a>Log in?</a></p>
  </section>

  <!-- Log in -->
  <section class="screen screen--login">
    <div class="abs logo logo--large">FlavorTrek</div>
    <div class="abs label" style="top:143px">Username</div>
    <div class="abs field field--active field--filled" style="top:158px">Marcus Lenn</div>
    <div class="abs label" style="top:212px">Password</div>
    <div class="abs field" style="top:228px">Enter your password
      <svg class="eye" width="14" height="12" viewBox="0 0 14 12"><path d="M1 6c2-3.5 10-3.5 12 0-2 3.5-10 3.5-12 0z" fill="none" stroke="#999" stroke-width="1"/><circle cx="7" cy="6" r="1.8" fill="none" stroke="#999"/><line x1="2" y1="11" x2="12" y2="1" stroke="#999"/></svg>
    </div>
    <div class="abs btn" style="top:276px">Login</div>
    <div class="abs forgot" style="top:314px">Forget Password?</div>
    <div class="abs divider" style="top:348px">Or Continue With</div>
    <div class="abs social" style="left:78px;top:399px">Orbly</div>
    <div class="abs social" style="left:129px;top:399px">Chatter</div>
    <div class="abs social" style="left:180px;top:399px">Pomme</div>
    <p class="abs footnote" style="top:494px">Don't have an account? <a>Sign Up Here</a></p>
  </section>

  <!-- Home -->
  <section class="screen screen--home">
    <div class="abs logo logo--small">FlavorTrek</div>
    <div class="abs icon-btn icon-btn--bell" style="left:196px;top:22px">
      <svg width="12" height="13" viewBox="0 0 12 13"><path d="M2 9.5V6a4 4 0 0 1 8 0v3.5l1 1H1z" fill="none" stroke="#fff" stroke-width="1"/><path d="M4.8 11.5a1.2 1.2 0 0 0 2.4 0" fill="none" stroke="#fff"/><circle cx="9" cy="3" r="2" fill="#e02424"/></svg>
    </div>
    <div class="abs icon-btn avatar" style="left:229px;top:22px" role="img" aria-label="User profile photo"></div>
    <div class="abs search-label">Search</div>
    <div class="abs search-box">Search
      <span class="search-go"><svg width="10" height="10" viewBox="0 0 10 10"><circle cx="4.2" cy="4.2" r="3" fill="none" stroke="#fff" stroke-width="1.2"/><line x1="6.5" y1="6.5" x2="9" y2="9" stroke="#fff" stroke-width="1.2"/></svg></span>
    </div>
    <div class="abs section-title" style="top:96px">Featured Recipes</div>

    <div class="abs recipe-photo tone-taco" style="left:18px;top:120px" role="img" aria-label="Tacos with lime and greens"></div>
    <div class="abs recipe-photo tone-potato" style="left:95px;top:120px" role="img" aria-label="Baked potatoes with herbs"></div>
    <div class="abs recipe-photo tone-stew" style="left:173px;top:120px" role="img" aria-label="Hands holding a bowl of stew"></div>
    <div class="abs recipe-photo tone-pasta" style="left:18px;top:212px" role="img" aria-label="Plate of spaghetti"></div>
    <div class="abs recipe-photo tone-chicken" style="left:95px;top:212px" role="img" aria-label="Grilled chicken with tomatoes"></div>
    <div class="abs recipe-photo tone-stirfry" style="left:173px;top:212px" role="img" aria-label="Bowl of chicken stir-fry"></div>

    <div class="abs recipe-name" style="left:17px;top:180px">Fajitas</div><div class="abs recipe-price" style="left:18px;top:191px">$2.50</div>
    <div class="abs recipe-name" style="left:94px;top:180px">Fajitas</div><div class="abs recipe-price" style="left:95px;top:191px">$2.50</div>
    <div class="abs recipe-name" style="left:173px;top:180px">Fajitas</div><div class="abs recipe-price" style="left:173px;top:191px">$2.50</div>
    <div class="abs recipe-name" style="left:17px;top:272px">Fajitas</div><div class="abs recipe-price" style="left:18px;top:283px">$2.50</div>
    <div class="abs recipe-name" style="left:94px;top:272px">Fajitas</div><div class="abs recipe-price" style="left:95px;top:283px">$2.50</div>
    <div class="abs recipe-name" style="left:173px;top:272px">Fajitas</div><div class="abs recipe-price" style="left:173px;top:283px">$2.50</div>

    <svg class="abs add" style="left:75px;top:191px" viewBox="0 0 12 12"><circle cx="6" cy="6" r="5.4" fill="none" stroke="#333" stroke-width=".8"/><path d="M6 3.5v5M3.5 6h5" stroke="#333"/></svg>
    <svg class="abs add" style="left:152px;top:191px" viewBox="0 0 12 12"><circle cx="6" cy="6" r="5.4" fill="none" stroke="#333" stroke-width=".8"/><path d="M6 3.5v5M3.5 6h5" stroke="#333"/></svg>
    <svg class="abs add" style="left:230px;top:191px" viewBox="0 0 12 12"><circle cx="6" cy="6" r="5.4" fill="none" stroke="#333" stroke-width=".8"/><path d="M6 3.5v5M3.5 6h5" stroke="#333"/></svg>
    <svg class="abs add" style="left:75px;top:283px" viewBox="0 0 12 12"><circle cx="6" cy="6" r="5.4" fill="none" stroke="#333" stroke-width=".8"/><path d="M6 3.5v5M3.5 6h5" stroke="#333"/></svg>
    <svg class="abs add" style="left:152px;top:283px" viewBox="0 0 12 12"><circle cx="6" cy="6" r="5.4" fill="none" stroke="#333" stroke-width=".8"/><path d="M6 3.5v5M3.5 6h5" stroke="#333"/></svg>
    <svg class="abs add" style="left:230px;top:283px" viewBox="0 0 12 12"><circle cx="6" cy="6" r="5.4" fill="none" stroke="#333" stroke-width=".8"/><path d="M6 3.5v5M3.5 6h5" stroke="#333"/></svg>

    <div class="abs section-title" style="top:311px">Popular Restaurants</div>
    <div class="abs venue-photo tone-hall" style="left:18px;top:335px" role="img" aria-label="Bright restaurant interior with wooden tables"></div>
    <div class="abs venue-photo tone-dining" style="left:133px;top:335px" role="img" aria-label="Warm dining room with orange curtains"></div>
    <div class="abs venue-name" style="left:17px;top:422px">Lotus Garden</div>
    <div class="abs venue-name" style="left:133px;top:422px">Marisco</div>

    <div class="abs promo">Subscribe to get premium options of<br>recipes and restaurants</div>
    <div class="abs btn btn--promo">Create Account</div>
  </section>
</body>
</html>
```